harvest Soon Book Cover Design for real estate investment book

I am looking for a Book Cover design for my new book. I would like designs for a hardcover, softcover and Lumora book.

The book deals with real estate and mortgage investments. Looking for a clean, bright simple design. Want to cover to be White with big RED letters. See "Dancing past Noon" book for an example ... see attached.

Target Market(s)

Affluent people with money looking for investment solutions.

Industry/Entity Type

Financial Service

Font styles to use
Serif

Requirements
Must have
• Bright clean design that will be appealing to affluent people.
• Title: harvest SOON
• Subtitle: A quiet method for thriving through land holdings
• subsubtitle: Secrets the Bank Teller Keeps Hidden From Clients...
• Author: Ned Falconby
• My Picture on the inside cover or on the back cover
• Book Description, Author description
Nice to have
• Focus on the Front cover look and feel first. Then we can look at the inside flaps and back cover. I will need to send you text. This is for the full cover. Front. Back. Spine. Inside flaps fro hardcover.

```html
<!DOCTYPE html>
<html lang="en">
<head>
<meta charset="utf-8">
<title>harvest SOON — Ned Falconby</title>
<link href="https://fonts.googleapis.com/css2?family=Anton&family=Cormorant+Garamond:wght@500&display=swap" rel="stylesheet">
<style>
  :root {
    --paper: #ebebeb;
    --paper-light: #f4f4f3;
    --paper-edge: #ffffff;
    --shadow: rgba(0,0,0,0.18);
    --red: #e8202a;
    --ink: #1a1a1a;
  }
  html, body {
    margin: 0;
    padding: 0;
    overflow: hidden;
    background: var(--paper);
  }
  .cover {
    position: relative;
    width: 848px;
    height: 1200px;
    overflow: hidden;
    background: linear-gradient(160deg, #efefef 0%, var(--paper) 60%, #e4e4e4 100%);
  }
  .cover-art {
    position: absolute;
    inset: 0;
    width: 848px;
    height: 1200px;
  }
  .title-text {
    font-family: "Anton", "Impact", sans-serif;
    fill: var(--red);
  }
  .author-name {
    font-family: "Cormorant Garamond", "Times New Roman", serif;
    font-weight: 500;
    fill: var(--ink);
    letter-spacing: 1px;
  }
</style>
</head>
<body>
<div class="cover">
  <svg class="cover-art" viewBox="0 0 848 1200" xmlns="http://www.w3.org/2000/svg">
    <defs>
      <filter id="tear-shadow" x="-10%" y="-10%" width="120%" height="120%">
        <feDropShadow dx="0" dy="2" stdDeviation="3" flood-color="#000" flood-opacity="0.12"/>
      </filter>
      <linearGradient id="curl-shade" x1="0" y1="0" x2="1" y2="0">
        <stop offset="0" stop-color="#d9d9d9"/>
        <stop offset="0.5" stop-color="#fafafa"/>
        <stop offset="1" stop-color="#cfcfcf"/>
      </linearGradient>
    </defs>

    <!-- main torn window -->
    <g class="torn-window" filter="url(#tear-shadow)">
      <path fill="var(--paper-edge)" d="M96 196 L140 188 L180 192 L230 184 L290 190 L340 183 L400 189 L460 182 L520 190 L580 184 L640 191 L700 185 L750 192 L770 205 L764 250 L772 300 L766 360 L774 420 L768 480 L775 540 L767 600 L773 660 L766 710 L770 748 L720 744 L660 751 L600 745 L540 752 L480 746 L420 753 L360 746 L300 752 L240 745 L180 751 L130 745 L94 748 L100 700 L92 640 L99 580 L91 520 L98 460 L90 400 L98 340 L92 280 L99 230 Z"/>
      <path fill="var(--paper-light)" d="M104 204 L145 197 L185 201 L232 193 L290 199 L342 192 L400 198 L460 191 L520 199 L580 193 L640 200 L700 194 L758 201 L756 250 L763 300 L757 360 L765 420 L759 480 L766 540 L758 600 L764 660 L757 705 L760 738 L720 735 L660 741 L600 736 L540 742 L480 737 L420 743 L360 737 L300 742 L240 736 L180 741 L130 736 L104 738 L109 700 L101 640 L108 580 L100 520 L107 460 L99 400 L107 340 L101 280 L108 232 Z"/>
    </g>

    <text class="title-text" x="137" y="429" font-size="240" textLength="583" lengthAdjust="spacingAndGlyphs">HARVEST</text>
    <text class="title-text" x="198" y="637" font-size="240" textLength="470" lengthAdjust="spacingAndGlyphs">SOON</text>
    <text class="title-text" x="152" y="723" font-size="21" textLength="556" lengthAdjust="spacingAndGlyphs">A QUIET METHOD FOR THRIVING THROUGH LAND HOLDINGS</text>

    <text class="author-name" x="424" y="838" font-size="38" text-anchor="middle" textLength="280" lengthAdjust="spacingAndGlyphs">NED FALCONBY</text>

    <!-- bottom torn strip -->
    <g class="torn-strip" filter="url(#tear-shadow)">
      <path fill="var(--paper-edge)" d="M70 942 L140 937 L220 941 L300 935 L380 940 L460 934 L540 939 L620 933 L700 938 L780 936 L776 960 L781 990 L776 1014 L700 1010 L620 1016 L540 1011 L460 1017 L380 1011 L300 1016 L220 1010 L140 1015 L70 1012 Z"/>
      <path fill="var(--paper-light)" d="M80 948 L140 944 L220 948 L300 942 L380 947 L460 941 L540 946 L620 940 L700 945 L770 943 L768 965 L772 990 L768 1007 L700 1003 L620 1009 L540 1004 L460 1010 L380 1004 L300 1009 L220 1003 L140 1008 L80 1005 Z"/>
    </g>
    <rect class="paper-curl" x="30" y="944" width="118" height="72" rx="22" fill="url(#curl-shade)" filter="url(#tear-shadow)"/>

    <text class="title-text" x="157" y="993" font-size="22" textLength="615" lengthAdjust="spacingAndGlyphs">SECRETS THE BANK TELLER KEEPS HIDDEN FROM CLIENTS...</text>
  </svg>
</div>
</body>
</html>
```